Harbourline Metro Business Racquet Circuit (est.1952)

The Metro Business Racquet Circuit began in 1952 and has been played every year since. It is the longest running continuous sporting competition in the Sydney CBD. It is a team squash competition from May to Oct yearly played between companies, sporting groups or just a groups of friends.
We are looking for a flyer that we can reuse every year (so the content within the flyer can't be tied to a specific time). Other specific we are looking for are
1. Squash imagery (can either be real or graphic design) depicting action / athleticism / friendly rivalry
2. Needs the following content
a ) "A Sydney CBD based competition for friendly rivalry between companies, sporting clubs or between friends"
b) "All matches in and around the CBD from 5.30pm to 8pm"
c) "We cater for all playing abilities"
d) "Ladies beginner comp includes complimentary coaching"
e) "Visit our website www.plvqn.org.au for more info or contact Walter on frontw@qmx.com.au"

Flyer needs to include the logos attached in file upload section

```html
<!DOCTYPE html>
<html lang="en">
<head>
<meta charset="utf-8">
<title>Harbourline Metro Business Racquet Circuit – Flyer</title>
<link rel="stylesheet" href="https://fonts.googleapis.com/css2?family=Lato:wght@400;700;900&family=Oswald:wght@500;600;700&family=Alfa+Slab+One&display=swap">
<style>
  :root {
    --red: #b5121b;
    --yellow: #f9b51a;
    --gold: #fcc21b;
    --navy: #13285c;
    --white: #ffffff;
    --page: #e9e9e9;
    --ink: #1d1d1f;
  }
  * { box-sizing: border-box; margin: 0; padding: 0; }
  html, body { width: 1200px; height: 1177px; overflow: hidden; }
  body { background: var(--page); font-family: "Lato", Arial, sans-serif; }

  .flyer {
    position: absolute; left: 257px; top: 82px;
    width: 720px; height: 1018px;
    background: var(--white);
    overflow: hidden;
  }

  /* header */
  .header-band {
    position: absolute; left: 0; top: 0; width: 720px; height: 155px;
    background: var(--red);
  }
  .header-text {
    position: absolute; left: 275px; top: 10px; width: 435px;
    text-align: center; color: var(--white);
  }
  .header-kicker { font-weight: 900; font-size: 18px; line-height: 22px; letter-spacing: .3px; }
  .header-promoting {
    display: flex; align-items: center; gap: 8px;
    color: var(--gold); font-weight: 900; font-size: 18px; line-height: 22px;
  }
  .header-promoting::before, .header-promoting::after {
    content: ""; flex: 1; height: 2px; background: var(--gold);
  }
  .header-title {
    font-family: "Alfa Slab One", Georgia, serif; font-weight: 400;
    font-size: 37px; line-height: 44px; letter-spacing: .5px;
  }
  .header-sub { font-weight: 900; font-size: 17px; line-height: 21px; }

  .brand-badge {
    position: absolute; left: -130px; top: -180px;
    width: 400px; height: 400px; border-radius: 50%;
    background: var(--white); border: 6px solid var(--yellow);
  }
  .brand-mark {
    position: absolute; left: 14px; top: 62px; width: 230px;
    display: flex; align-items: center; gap: 10px;
    color: var(--navy); font-weight: 900; font-size: 25px; line-height: 1.05;
  }
  .brand-mark .dot {
    flex: none; width: 34px; height: 34px; border-radius: 50%; background: var(--navy);
  }

  /* photo */
  .action-photo {
    position: absolute; left: 0; top: 162px; width: 720px; height: 380px;
    background: linear-gradient(100deg, #d9d7d3 0%, #c9c6c0 35%, #b9b4ad 60%, #cfccc6 100%);
  }

  .waves { position: absolute; left: 0; top: 0; }

  /* league title */
  .league {
    position: absolute; left: 0; top: 553px; width: 720px;
    text-align: center; font-family: "Oswald", "Arial Narrow", sans-serif;
  }
  .league-line {
    color: var(--white); font-weight: 600; font-size: 30px; line-height: 37px; letter-spacing: .5px;
  }
  .league-line .star { color: var(--red); font-size: 22px; vertical-align: 3px; }
  .league-name {
    color: var(--red); font-weight: 600; font-size: 56px; line-height: 74px;
    white-space: nowrap; letter-spacing: 0;
  }

  /* details */
  .details-left {
    position: absolute; left: 20px; top: 778px; width: 270px;
    text-align: center; color: var(--white);
  }
  .details-where { font-weight: 900; font-size: 20px; line-height: 24px; }
  .details-time {
    font-family: "Oswald", "Arial Narrow", sans-serif; font-weight: 500;
    font-size: 26px; line-height: 34px; margin-top: 4px;
  }
  .details-time em { font-style: normal; color: var(--gold); }

  .feature-list { position: absolute; left: 322px; top: 772px; width: 390px; list-style: none; }
  .feature {
    display: flex; align-items: center; gap: 14px; margin-bottom: 14px;
    color: var(--white); font-size: 16px; line-height: 20px;
  }
  .feature strong { display: block; color: var(--gold); font-weight: 900; font-size: 17px; }
  .tick { flex: none; width: 42px; height: 42px; }

  /* contact */
  .contact {
    position: absolute; left: 0; top: 886px; width: 720px; height: 62px;
    background: var(--red); color: var(--white);
    border-top: 3px solid var(--white);
    text-align: center; font-weight: 900; font-size: 17px; line-height: 24px;
    padding-top: 6px;
  }
  .contact em { font-style: normal; color: var(--gold); }

  /* partners */
  .partners {
    position: absolute; left: 0; top: 948px; width: 720px; height: 70px;
    background: var(--white); border-top: 4px solid var(--red);
    display: flex; align-items: center; justify-content: center; gap: 24px;
  }
  .partner { display: flex; align-items: center; gap: 8px; color: var(--ink); font-weight: 700; font-size: 12px; }
  .partner .dot { width: 32px; height: 32px; border-radius: 50%; background: var(--navy); }
  .partner-seal { width: 44px; height: 44px; border-radius: 50%; background: var(--navy); border: 3px solid var(--gold); }
</style>
</head>
<body>
  <main class="flyer">
    <div class="header-band"></div>

    <div role="img" aria-label="Photo of four smiling squash players in a court, racquets ready, mid-rally" class="action-photo"></div>

    <svg class="waves" width="720" height="1018" viewBox="0 0 720 1018" aria-hidden="true">
      <path d="M0 494 C 240 522, 480 500, 720 430 L720 1018 L0 1018 Z" fill="var(--red)"/>
      <path d="M0 520 C 240 546, 480 526, 720 456 L720 1018 L0 1018 Z" fill="var(--yellow)"/>
      <path d="M0 736 C 200 702, 450 690, 720 742 L720 1018 L0 1018 Z" fill="var(--red)"/>
      <path d="M0 750 C 200 716, 450 706, 720 766 L720 1018 L0 1018 Z" fill="var(--navy)"/>
    </svg>

    <div class="brand-badge"></div>
    <div class="brand-mark"><span class="dot"></span><span>METRO COURT SQUASH</span></div>

    <header class="header-text">
      <p class="header-kicker">A SYDNEY CBD BASED LEAGUE</p>
      <p class="header-promoting">PROMOTING</p>
      <h2 class="header-title">FRIENDLY RIVALRY</h2>
      <p class="header-sub">BETWEEN COMPANIES, SPORTING CLUBS<br>AND FRIENDS</p>
    </header>

    <section class="league">
      <p class="league-line">HARBOURLINE</p>
      <p class="league-line">METRO <span class="star">★</span></p>
      <h1 class="league-name">BUSINESS RACQUET CIRCUIT</h1>
    </section>

    <section class="details-left">
      <p class="details-where">ALL MATCHES IN AND<br>AROUND THE CBD</p>
      <p class="details-time">FROM <em>5.30PM TO 8PM</em></p>
    </section>

    <ul class="feature-list">
      <li class="feature">
        <svg class="tick" viewBox="0 0 42 42" aria-hidden="true">
          <rect x="3" y="8" width="31" height="31" fill="none" stroke="var(--white)" stroke-width="3"/>
          <path d="M10 22 L18 31 L38 4" fill="none" stroke="var(--white)" stroke-width="5" stroke-linecap="square"/>
        </svg>
        <span>We cater for<strong>ALL PLAYING ABILITIES</strong></span>
      </li>
      <li class="feature">
        <svg class="tick" viewBox="0 0 42 42" aria-hidden="true">
          <rect x="3" y="8" width="31" height="31" fill="none" stroke="var(--white)" stroke-width="3"/>
          <path d="M10 22 L18 31 L38 4" fill="none" stroke="var(--white)" stroke-width="5" stroke-linecap="square"/>
        </svg>
        <span>Ladies beginner comp includes<strong>COMPLIMENTARY COACHING</strong></span>
      </li>
    </ul>

    <footer class="contact">
      VISIT OUR WEBSITE <em>WWW.PLVQN.ORG.AU</em><br>
      FOR MORE INFO OR CONTACT WALTER ON <em>FRONTW@QMX.COM.AU</em>
    </footer>

    <section class="partners">
      <div class="partner"><span class="dot"></span><span>HCRA</span></div>
      <div class="partner"><span>HARBOUR COURTS RACQUETS ASSOCIATION</span></div>
      <div class="partner"><span class="dot"></span><span>BAYSIDE RACQUET ACADEMY</span></div>
      <div class="partner-seal"></div>
    </section>
  </main>
</body>
</html>
```